Velorine Jewellery Display Card

We are a jewellery manufacturer and need artwork for an A4 size strut card to advertise our new "Crescent Loop Pendant "
In the attached files is a picture of the new pendant and artwork for our trademark "Velorine"
We also need to include the phrase " an expression of love "
as part of the artwork.
The background colour should be predominately white

Target Market(s)

This product has been designed as a gift for Mothers as it has their children names
engraved on the pendant

Industry/Entity Type

Manufacturer

Font styles to use
Serif
Script

Colors
ffffff

Requirements
Must have
• Artwork should be simple and elegant , the predominant look in Australian jewellery stores which is where these display cards will be is white, bright and elegant

```html
<!DOCTYPE html>
<html lang="en">
<head>
<meta charset="utf-8">
<title>Velorine Crescent Loop Pendant – Display Card Options</title>
<link href="https://fonts.googleapis.com/css2?family=Lato:wght@300&family=Source+Sans+3:wght@400&family=Dosis:wght@400&family=Dancing+Script:wght@700&display=swap" rel="stylesheet">
<style>
  :root {
    --board-dark: #9c9c9c;
    --board-light: #cbcbcb;
    --card: #ffffff;
    --grey-text: #8e8e8e;
    --logo-grey: #a9a9a9;
    --berry: #8a1457;
    --metal-light: #f4f4f4;
    --metal-mid: #d0d0d0;
    --metal-dark: #9a9a9a;
  }
  * { margin: 0; padding: 0; box-sizing: border-box; }
  html, body { width: 973px; height: 1200px; overflow: hidden; }
  body {
    position: relative;
    background: linear-gradient(120deg, var(--board-dark) 0%, var(--board-light) 45%, var(--board-dark) 100%);
  }
  .option-card {
    position: absolute;
    width: 407px;
    height: 572px;
    background: var(--card);
  }
  .card-5 { left: 65px; top: 18px; }
  .card-6 { left: 498px; top: 18px; }
  .card-7 { left: 65px; top: 615px; }
  .card-8 { left: 498px; top: 615px; }

  .brand-name, .product-name, .tagline, .pendant-photo {
    position: absolute;
    left: 0; right: 0;
    text-align: center;
  }
  .brand-name {
    font-family: "Lato", sans-serif;
    font-weight: 300;
    font-size: 45px;
    letter-spacing: 2px;
    color: var(--logo-grey);
    line-height: 1;
  }
  .product-name {
    font-family: "Source Sans 3", sans-serif;
    font-size: 17.5px;
    letter-spacing: 0.6px;
    color: var(--grey-text);
    line-height: 1;
  }
  .tagline {
    font-family: "Dosis", sans-serif;
    font-size: 19px;
    letter-spacing: 2px;
    color: var(--grey-text);
    line-height: 1;
  }
  .tagline .love {
    font-family: "Dancing Script", cursive;
    font-weight: 700;
    font-size: 25px;
    letter-spacing: 0;
    color: var(--berry);
  }
  .underlined span.rule-text {
    display: inline-block;
    padding-bottom: 6px;
    border-bottom: 1px solid var(--berry);
  }
  .pendant-photo {
    margin: 0 auto;
    width: 172px;
    height: 222px;
    border-radius: 50% 50% 48% 48% / 56% 56% 44% 44%;
    background: radial-gradient(ellipse at 45% 40%, var(--metal-light) 0%, var(--metal-mid) 60%, var(--metal-dark) 100%);
  }

  .option-label {
    position: absolute;
    font-family: "Dosis", sans-serif;
    font-size: 44px;
    letter-spacing: 2px;
    color: var(--berry);
    line-height: 1;
    white-space: nowrap;
    transform-origin: left top;
    transform: rotate(-90deg);
  }
  .label-5 { left: 10px; top: 590px; }
  .label-6 { left: 910px; top: 590px; }
  .label-7 { left: 10px; top: 1188px; }
  .label-8 { left: 910px; top: 1188px; }
</style>
</head>
<body>

  <section class="option-card card-5">
    <div class="brand-name" style="top:46px;">VELORINE</div>
    <div class="product-name" style="top:148px;">CRESCENT LOOP PENDANT</div>
    <div class="pendant-photo" style="top:186px;" role="img" aria-label="Photo of the silver Crescent Loop Pendant with engraved children's names"></div>
    <div class="tagline" style="top:460px;">An expression of <span class="love">love</span></div>
  </section>

  <section class="option-card card-6">
    <div class="brand-name" style="top:46px;">VELORINE</div>
    <div class="tagline" style="top:136px;">An expression of <span class="love">love</span></div>
    <div class="pendant-photo" style="top:186px;" role="img" aria-label="Photo of the silver Crescent Loop Pendant with engraved children's names"></div>
    <div class="product-name underlined" style="top:472px;"><span class="rule-text">CRESCENT LOOP PENDANT</span></div>
  </section>

  <section class="option-card card-7">
    <div class="product-name" style="top:68px;">CRESCENT LOOP PENDANT</div>
    <div class="pendant-photo" style="top:136px;" role="img" aria-label="Photo of the silver Crescent Loop Pendant with engraved children's names"></div>
    <div class="tagline underlined" style="top:409px;"><span class="rule-text">An expression of <span class="love">love</span></span></div>
    <div class="brand-name" style="top:500px;">VELORINE</div>
  </section>

  <section class="option-card card-8">
    <div class="tagline" style="top:64px;">An expression of <span class="love">love</span></div>
    <div class="pendant-photo" style="top:136px;" role="img" aria-label="Photo of the silver Crescent Loop Pendant with engraved children's names"></div>
    <div class="product-name" style="top:415px;">CRESCENT LOOP PENDANT</div>
    <div class="brand-name" style="top:500px;">VELORINE</div>
  </section>

  <div class="option-label label-5">Option 5</div>
  <div class="option-label label-6">Option 6</div>
  <div class="option-label label-7">Option 7</div>
  <div class="option-label label-8">Option 8</div>

</body>
</html>
```